Birch Harbor Group Biz cards and Stationery
Oil & Gas industry
Great start! Can we see some designs with the logo faded into the background as well?
Please see our logo that we just finalized. Waiting for the file to upload. Thanks!

```html
<!DOCTYPE html>
<html lang="en">
<head>
<meta charset="utf-8">
<title>Birch Harbor Group – Business Cards</title>
<link rel="stylesheet" href="https://fonts.googleapis.com/css2?family=Open+Sans:wght@400;600;700&display=swap">
<style>
  :root {
    --bg: #e9e6e1;
    --card: #ffffff;
    --blue: #1f6fc6;
    --blue-dark: #15539a;
    --green: #7cc242;
    --ink: #3a3a3a;
    --muted: #5c5c5c;
    --rule: #c9c9c9;
  }
  * { box-sizing: border-box; margin: 0; padding: 0; }
  html, body { width: 1200px; height: 852px; overflow: hidden; }
  body {
    background: var(--bg);
    font-family: "Open Sans", sans-serif;
    color: var(--ink);
    position: relative;
  }
  .card {
    position: absolute;
    width: 520px;
    height: 300px;
    background: var(--card);
    border-radius: 18px;
    overflow: hidden;
    box-shadow: 0 6px 18px rgba(0,0,0,.18);
  }
  .card--classic { left: 110px; top: 90px; }
  .card--centered { left: 570px; top: 462px; }

  .swoosh { position: absolute; left: 0; bottom: 0; width: 520px; height: 110px; }

  .brand { display: flex; flex-direction: column; align-items: center; gap: 10px; }
  .brand__mark { width: 56px; height: 56px; border-radius: 50%; background: var(--blue); }
  .brand__name {
    font-weight: 700; color: var(--blue); font-size: 19px;
    text-align: center; line-height: 1.15; letter-spacing: .5px;
  }

  .person__name { color: var(--blue); font-weight: 700; font-size: 19px; line-height: 1.2; }
  .person__title { color: var(--green); font-weight: 600; font-size: 12.5px; margin-bottom: 12px; }
  .address { font-size: 12.5px; line-height: 1.45; color: var(--muted); }

  .contacts { list-style: none; font-size: 12.5px; color: var(--muted); }
  .contacts li { display: flex; align-items: center; gap: 8px; height: 19px; }
  .contacts svg { width: 12px; height: 12px; flex: none; }

  /* classic layout */
  .card--classic .brand { position: absolute; left: 22px; top: 70px; width: 200px; }
  .card--classic .divider {
    position: absolute; left: 238px; top: 28px; width: 1px; height: 190px; background: var(--rule);
  }
  .card--classic .details { position: absolute; left: 256px; top: 26px; }
  .card--classic .contacts { margin-top: 14px; }

  /* centered layout */
  .card--centered .brand { position: absolute; left: 0; right: 0; top: 22px; }
  .card--centered .brand__name { font-size: 18px; }
  .card--centered .details { position: absolute; right: 280px; top: 150px; text-align: right; }
  .card--centered .person__title { margin-bottom: 6px; }
  .card--centered .divider {
    position: absolute; left: 256px; top: 150px; width: 1px; height: 84px; background: var(--rule);
  }
  .card--centered .contacts { position: absolute; left: 270px; top: 150px; }
</style>
</head>
<body>

<!-- Card layout A: logo left, details right -->
<article class="card card--classic">
  <svg class="swoosh" viewBox="0 0 520 110" preserveAspectRatio="none" aria-hidden="true">
    <path d="M0 110 L0 104 C160 100 360 80 520 20 L520 110 Z" fill="var(--blue)"/>
    <path d="M0 96 C170 94 360 72 520 4 L520 14 C360 80 170 100 0 100 Z" fill="var(--green)"/>
  </svg>

  <div class="brand">
    <span class="brand__mark"></span>
    <span class="brand__name">BIRCH HARBOR<br>GROUP, LLC</span>
  </div>

  <span class="divider"></span>

  <div class="details">
    <p class="person__name">Owen Mercer</p>
    <p class="person__title">Managing Partner</p>
    <p class="address">418 Larchmont Ridge Road<br>Bellhaven, PA 15290</p>
    <ul class="contacts">
      <li><svg viewBox="0 0 12 12"><path d="M3 1l2 2-1 2 3 3 2-1 2 2-2 2C5 11 1 7 1 3z" fill="var(--blue)"/></svg>(555) 210-4471</li>
      <li><svg viewBox="0 0 12 12"><rect x="3" y="0.5" width="6" height="11" rx="1.2" fill="var(--blue)"/><rect x="4" y="2" width="4" height="6" fill="#fff"/></svg>(555) 362-9038</li>
      <li><svg viewBox="0 0 12 12"><circle cx="6" cy="6" r="5" fill="none" stroke="var(--blue)" stroke-width="1.4"/><circle cx="6" cy="6" r="2" fill="none" stroke="var(--blue)" stroke-width="1.4"/></svg>owen@birchharborgroup.com</li>
      <li><svg viewBox="0 0 12 12"><circle cx="6" cy="6" r="5" fill="none" stroke="var(--blue)" stroke-width="1.2"/><path d="M1 6h10M6 1c-3 3-3 7 0 10M6 1c3 3 3 7 0 10" fill="none" stroke="var(--blue)" stroke-width="1"/></svg>www.birchharborgroup.com</li>
    </ul>
  </div>
</article>

<!-- Card layout B: logo top centre, split details -->
<article class="card card--centered">
  <svg class="swoosh" viewBox="0 0 520 110" preserveAspectRatio="none" aria-hidden="true">
    <path d="M520 110 L520 104 C360 100 160 80 0 20 L0 110 Z" fill="var(--blue)"/>
    <path d="M520 96 C350 94 160 72 0 4 L0 14 C160 80 350 100 520 100 Z" fill="var(--green)"/>
  </svg>

  <div class="brand">
    <span class="brand__mark"></span>
    <span class="brand__name">BIRCH HARBOR GROUP, LLC</span>
  </div>

  <div class="details">
    <p class="person__name">Owen Mercer</p>
    <p class="person__title">Managing Partner</p>
    <p class="address">418 Larchmont Ridge Road<br>Bellhaven, PA 15290</p>
  </div>

  <span class="divider"></span>

  <ul class="contacts">
    <li><svg viewBox="0 0 12 12"><path d="M3 1l2 2-1 2 3 3 2-1 2 2-2 2C5 11 1 7 1 3z" fill="var(--blue)"/></svg>(555) 210-4471</li>
    <li><svg viewBox="0 0 12 12"><rect x="3" y="0.5" width="6" height="11" rx="1.2" fill="var(--blue)"/><rect x="4" y="2" width="4" height="6" fill="#fff"/></svg>(555) 362-9038</li>
    <li><svg viewBox="0 0 12 12"><circle cx="6" cy="6" r="5" fill="none" stroke="var(--blue)" stroke-width="1.4"/><circle cx="6" cy="6" r="2" fill="none" stroke="var(--blue)" stroke-width="1.4"/></svg>owen@birchharborgroup.com</li>
    <li><svg viewBox="0 0 12 12"><circle cx="6" cy="6" r="5" fill="none" stroke="var(--blue)" stroke-width="1.2"/><path d="M1 6h10M6 1c-3 3-3 7 0 10M6 1c3 3 3 7 0 10" fill="none" stroke="var(--blue)" stroke-width="1"/></svg>www.birchharborgroup.com</li>
  </ul>
</article>

</body>
</html>
```